Business Card for Marco Tindley Analytics and Marco Tindley Photography

I want a double sided business card: on one side it should be about "Marco Tindley Photography" and on the other side about "Marco Tindley Analytics". You find the logos for these two projects in the attachments. The design of the business card should blend well with the colours and fonts used in the logos and should be quite simple, yet look professional and modern.

In addition to my name, there should be content for a telephone number, e-mail address and website. There should be little icons (for telephone, email and web) before these fields. I do not want a postal mail address field.
Lastly you should indicate that people can contact me in the following languages: Lëtzebuergesch, Deutsch, Français, English, Castellano, Ido
This should be very unobtrusive: either in a small muted font or with little icons (preferably without using flags as flags represent nations, not languages - one possibility would be by using the 2 letter ISO codes).

The design should be delivered in Adobe Illustrator format or something similar that I can edit easily, as it's possible that I will change my e-mail address and domain soon.

I hope this was detailed enough but still leaves you some freedom for designing something nice.

Thank you!
Marco

Industry/Entity Type

Business

Contact Information for Business Card

e-mail address: mjt_@fernpost.example
website: www.marcotindley.example (for Marco Tindley Photography)
website: quarrynet.example/mjt (for Marco Tindley Analytics - this address is likely to change)
phone: +352 648 907 215 (not my real number - I prefer not to publish it on the web)

Requirements
Nice to have
• A speech bubble followed by the 2-letter language codes (lb, de, fr, en, es, io) or even speech bubble icons for every language would be nice and eliminates the need to put text like 'you can contact me in the following languages'.

```html
<!DOCTYPE html>
<html lang="en">
<head>
<meta charset="utf-8">
<title>Marco Tindley – Business Cards</title>
<link rel="stylesheet" href="https://fonts.googleapis.com/css2?family=Tinos:wght@400;700&display=swap">
<style>
  :root {
    --page: #2a2a2c;
    --card-dark: #231f20;
    --card-light: #ffffff;
    --accent-blue: #1ea0e0;
    --accent-orange: #f28c28;
    --accent-green: #1aa34a;
    --lang-green: #6dbb45;
    --ink-dark: #1a1a1a;
    --ink-light: #ffffff;
    --grey: #4d5155;
    --divider-dark: #6a6a6a;
    --divider-light: #777777;
  }
  html, body {
    margin: 0;
    padding: 0;
    width: 1200px;
    height: 1200px;
    overflow: hidden;
    background: var(--page);
    font-family: "Tinos", "Times New Roman", serif;
  }
  .card {
    position: absolute;
    left: 120px;
    width: 960px;
    height: 540px;
    box-sizing: border-box;
    box-shadow: 0 10px 30px rgba(0,0,0,0.5);
  }
  .card--photography { top: 40px; background: var(--card-dark); color: var(--ink-light); }
  .card--analytics { top: 620px; background: var(--card-light); color: var(--ink-dark); }

  .corner {
    position: absolute;
    width: 52px;
    height: 34px;
    border-color: var(--accent-blue);
    border-style: solid;
    border-width: 0;
  }
  .corner--tl { top: 28px; left: 36px; border-top-width: 4px; border-left-width: 4px; }
  .corner--tr { top: 28px; right: 36px; border-top-width: 4px; border-right-width: 4px; }
  .corner--bl { bottom: 28px; left: 36px; border-bottom-width: 4px; border-left-width: 4px; }
  .corner--br { bottom: 28px; right: 36px; border-bottom-width: 4px; border-right-width: 4px; }

  .brand {
    position: absolute;
    display: flex;
    align-items: center;
    gap: 18px;
  }
  .brand__dot {
    width: 26px;
    height: 26px;
    border-radius: 50%;
    background: var(--accent-orange);
    flex: none;
  }
  .brand__name {
    margin: 0;
    font-size: 44px;
    line-height: 1.12;
    color: var(--accent-orange);
    font-weight: 400;
  }
  .card--photography .brand { left: 110px; top: 215px; }
  .card--analytics .brand { left: 100px; top: 145px; }

  .divider {
    position: absolute;
    width: 2px;
  }
  .card--photography .divider { left: 540px; top: 150px; height: 230px; background: linear-gradient(to bottom, transparent, var(--divider-dark), transparent); }
  .card--analytics .divider { left: 560px; top: 90px; height: 230px; background: linear-gradient(to bottom, transparent, var(--divider-light), transparent); }

  .contacts {
    position: absolute;
    list-style: none;
    margin: 0;
    padding: 0;
  }
  .card--photography .contacts { left: 580px; top: 180px; }
  .card--analytics .contacts { left: 600px; top: 110px; }
  .contact {
    display: flex;
    align-items: center;
    gap: 16px;
    height: 56px;
    font-size: 25px;
    letter-spacing: 0.5px;
    white-space: nowrap;
  }
  .contact__icon {
    width: 38px;
    height: 38px;
    flex: none;
    color: var(--accent-orange);
  }
  .contact__icon .ring { fill: none; stroke: currentColor; stroke-width: 2.5; }
  .contact__icon .glyph { fill: none; stroke: currentColor; stroke-width: 2; stroke-linejoin: round; }
  .card--photography .contact__icon .glyph-fill { fill: currentColor; }
  .card--photography .contact__icon .glyph-fill + .glyph { stroke: var(--card-dark); }
  .contact__icon .glyph-fill { fill: none; }

  .languages {
    position: absolute;
    left: 60px;
    top: 370px;
    right: 60px;
  }
  .languages__intro {
    margin: 0 0 18px 10px;
    font-size: 22px;
  }
  .languages__list {
    list-style: none;
    margin: 0;
    padding: 0;
    display: flex;
    gap: 16px;
  }
  .lang {
    position: relative;
    padding: 6px 14px 8px;
    border-radius: 9px;
    color: var(--ink-light);
    font-size: 21px;
    background: var(--bubble);
  }
  .lang::after {
    content: "";
    position: absolute;
    right: 18px;
    bottom: -10px;
    border-left: 12px solid transparent;
    border-top: 11px solid var(--bubble);
  }
  .lang--lb { --bubble: var(--lang-green); }
  .lang--de { --bubble: var(--accent-orange); }
  .lang--fr { --bubble: var(--accent-green); }
  .lang--en { --bubble: var(--ink-dark); }
  .lang--es { --bubble: var(--grey); }
  .lang--io { --bubble: var(--accent-orange); }
</style>
</head>
<body>

<section class="card card--photography" aria-label="Photography side">
  <span class="corner corner--tl"></span>
  <span class="corner corner--tr"></span>
  <span class="corner corner--bl"></span>
  <span class="corner corner--br"></span>

  <div class="brand">
    <span class="brand__dot"></span>
    <h1 class="brand__name">Marco Tindley<br>Photography</h1>
  </div>

  <span class="divider"></span>

  <ul class="contacts">
    <li class="contact">
      <svg class="contact__icon" viewBox="0 0 40 40" aria-hidden="true">
        <circle class="ring" cx="20" cy="20" r="18"/>
        <circle class="glyph-fill" cx="20" cy="20" r="14"/>
        <g class="glyph"><path d="M10 17 q10 -7 20 0 v3 h-5 v-3 q-5 -2 -10 0 v3 h-5 z"/><rect x="13" y="21" width="14" height="8" rx="2"/></g>
      </svg>+352 648 907 215</li>
    <li class="contact">
      <svg class="contact__icon" viewBox="0 0 40 40" aria-hidden="true">
        <circle class="ring" cx="20" cy="20" r="18"/>
        <circle class="glyph-fill" cx="20" cy="20" r="14"/>
        <g class="glyph"><rect x="11" y="14" width="18" height="12" rx="1"/><path d="M11 14 l9 7 l9 -7"/></g>
      </svg>mjt_@fernpost.example</li>
    <li class="contact">
      <svg class="contact__icon" viewBox="0 0 40 40" aria-hidden="true">
        <circle class="ring" cx="20" cy="20" r="18"/>
        <circle class="glyph-fill" cx="20" cy="20" r="14"/>
        <g class="glyph"><circle cx="20" cy="20" r="9.5"/><ellipse cx="20" cy="20" rx="4" ry="9.5"/><path d="M10.5 20 h19 M12.5 15 h15 M12.5 25 h15"/></g>
      </svg>www.marcotindley.example</li>
  </ul>
</section>

<section class="card card--analytics" aria-label="Analytics side">
  <div class="brand">
    <span class="brand__dot"></span>
    <h1 class="brand__name">Marco Tindley<br>Analytics</h1>
  </div>

  <span class="divider"></span>

  <ul class="contacts">
    <li class="contact">
      <svg class="contact__icon" viewBox="0 0 40 40" aria-hidden="true">
        <circle class="ring" cx="20" cy="20" r="18"/>
        <g class="glyph"><path d="M10 17 q10 -7 20 0 v3 h-5 v-3 q-5 -2 -10 0 v3 h-5 z"/><rect x="13" y="21" width="14" height="8" rx="2"/></g>
      </svg>+352 648 907 215</li>
    <li class="contact">
      <svg class="contact__icon" viewBox="0 0 40 40" aria-hidden="true">
        <circle class="ring" cx="20" cy="20" r="18"/>
        <g class="glyph"><rect x="11" y="14" width="18" height="12" rx="1"/><path d="M11 14 l9 7 l9 -7"/></g>
      </svg>mjt_@fernpost.example</li>
    <li class="contact">
      <svg class="contact__icon" viewBox="0 0 40 40" aria-hidden="true">
        <circle class="ring" cx="20" cy="20" r="18"/>
        <g class="glyph"><circle cx="20" cy="20" r="9.5"/><ellipse cx="20" cy="20" rx="4" ry="9.5"/><path d="M10.5 20 h19 M12.5 15 h15 M12.5 25 h15"/></g>
      </svg>quarrynet.example/mjt</li>
  </ul>

  <div class="languages">
    <p class="languages__intro">You can contact me in the following languages</p>
    <ul class="languages__list">
      <li class="lang lang--lb">Lëtzebuergesch</li>
      <li class="lang lang--de">Deutsch</li>
      <li class="lang lang--fr">Français</li>
      <li class="lang lang--en">English</li>
      <li class="lang lang--es">Castellano</li>
      <li class="lang lang--io">Ido</li>
    </ul>
  </div>
</section>

</body>
</html>
```